A resource brochure for seniors and their families/Maplecrest Resource Group

As we age, the journey can come with unexpected challenges and obstacles. Maplecrest Resource Group is here to provide seniors and their families with a road map to navigate those challenges and insure the journey is as smooth as possible. We are a company that offers 'one stop shop' resources for seniors who need assistance with selling their home, need home care support or need to find suitable senior housing living choices and much more. We need this brochure to showcase a caring, clear and clear way for families or individuals, many who have just lost a spouse/parent, to find resources during a very difficult and confusing time in their life. The final design should communicate caring support, a call to action (call us!), and showcase a professional and knowledgeable team that will gently support and be a guide to families and individuals who are trying to make big life choices within the senior care arena.
Updates

Project Deadline Extended Reason: To give more time for designers as the initial window seemed a little too short. Thank you!!! Added Friday, March 20, 2015

Target Market(s)

A mature market- SENIORS (75+) and their families (adult children 50+) who typically are going through life changes such as losing a spouse or having to make a move from their home into a Retirement Community.

Industry/Entity Type

Group

Font styles to use
Serif
Script

Requirements
Must have
• Showcase a thoughtful and caring mentality- 'we will take care of you" in a professional and knowledgeable way. Please make it clear what the message is - we can assist with selling a home, bringing support and care into the home, find more appropriate housing as well as any resources or tools needed throughout the senior care spectrum of resources. Must have our name, logo, website and address and we need one panel to be laid out as a mailer- our address on top left. (Please see attached rough draft for address- thank you!) Also- please keep the testimonial, which is attached inclusive of additional verbiage.
Nice to have
• An attractive senior (female) on the cover of the brochure with a 'What's Next?" feel to engage people to open the collateral and relate to the story and purpose of what we do. Showcase what our services are- we are a company that guides families to and through much needed resources as it relates to aging and the ever-changing needs of an elderly person. We want to be the experts and trusted by our clients and the tough decisions that come along with aging. We offer our referral services at no cost to our clients.
Should not have
• Should not sound slick, 'sales-y' or too pushy- we are trying to build a relationship and not 'over sell'...we want to be a trusted resource guide and a helping hand.

```html
<!DOCTYPE html>
<html lang="en">
<head>
<meta charset="utf-8">
<title>Maplecrest Senior Resource Group – Brochure</title>
<link href="https://fonts.googleapis.com/css2?family=Cinzel:wght@400;700&family=Arimo:wght@400&family=Roboto:wght@300;400&display=swap" rel="stylesheet">
<style>
  :root {
    --slate: #474b6b;
    --slate-dark: #3f4363;
    --gold: #fbb624;
    --gold-deep: #f5a81a;
    --ink: #1f1f1f;
    --body-grey: #3a3a3a;
    --panel-white: #ffffff;
    --panel-grey: #e9e9ea;
    --stage: #eceae6;
  }
  * { margin: 0; padding: 0; box-sizing: border-box; }
  html, body { width: 1200px; height: 943px; overflow: hidden; background: var(--stage); }
  .canvas { position: relative; width: 1200px; height: 943px; }
  .brochure {
    position: absolute; left: 35px; top: 35px; width: 1128px; height: 871px;
    background: var(--panel-white); box-shadow: 0 3px 10px rgba(0,0,0,.25);
  }
  .panel { position: absolute; top: 0; height: 871px; overflow: hidden; }

  /* Left panel */
  .panel--story { left: 0; width: 373px; }
  .story-text {
    height: 515px; padding: 4px 10px 0 14px;
    background: linear-gradient(to bottom, #fff 0%, #fff 55%, #e6e6e6 100%);
    font-family: "Arimo", Arial, sans-serif; font-size: 17.4px; line-height: 39.3px; color: var(--ink);
  }
  .story-photo {
    height: 356px;
    background: linear-gradient(120deg, #e6e0d8 0%, #c9c3bb 35%, #8aa0c8 65%, #6d84b4 100%);
  }

  /* Middle panel */
  .panel--services {
    left: 373px; width: 379px;
    background: linear-gradient(to bottom, #fafafa 0%, #f2f2f3 50%, var(--panel-grey) 100%);
  }
  .services-head {
    margin-top: 3px; height: 57px; background: var(--slate);
    color: #fff; font-family: "Roboto", Arial, sans-serif; font-weight: 300;
    font-size: 30px; line-height: 57px; text-align: center;
  }
  .services-title {
    margin-top: 27px; text-align: center; color: var(--slate);
    font-family: "Cinzel", Georgia, serif; font-size: 31px; letter-spacing: 1px;
  }
  .services-intro {
    margin-top: 14px; text-align: center; color: #333;
    font-family: "Roboto", Arial, sans-serif; font-weight: 300; font-style: italic;
    font-size: 24px; line-height: 37px;
  }
  .services-list {
    list-style: none; margin: 22px 0 0 44px;
    font-family: "Roboto", Arial, sans-serif; font-weight: 300; font-size: 19.5px; color: #222;
  }
  .services-list li { line-height: 37px; margin-bottom: 17px; }
  .services-list li::before { content: "\2022"; margin-right: 5px; }
  .services-list .cont { display: block; padding-left: 14px; }

  .brand {
    position: absolute; left: 0; width: 100%; text-align: center;
    font-family: "Cinzel", Georgia, serif; color: var(--slate);
  }
  .brand-mark {
    display: block; width: 26px; height: 26px; margin: 0 auto 8px;
    border-radius: 50%; background: var(--slate);
  }
  .brand-name { display: block; font-size: 28px; line-height: 34px; }
  .brand-sub { display: block; font-size: 19px; line-height: 28px; }
  .panel--services .brand { top: 608px; }

  .address {
    position: absolute; top: 754px; width: 100%; text-align: center;
    font-family: "Arimo", Arial, sans-serif; font-size: 17.5px; line-height: 24px; color: #222;
  }
  .contact-band {
    position: absolute; left: 0; bottom: 0; width: 100%; height: 60px; background: var(--slate);
    color: #fff; text-align: center; font-family: "Arimo", Arial, sans-serif; font-size: 19.5px; line-height: 26px; padding-top: 4px;
  }

  /* Right panel (cover) */
  .panel--cover { left: 752px; width: 376px; background: var(--panel-white); }
  .panel--cover .brand { top: 28px; }
  .cover-photo {
    position: absolute; left: 0; top: 170px; width: 376px; height: 435px;
    background: linear-gradient(to bottom, #ffffff 0%, #efe6d6 25%, #e2cfae 50%, #f1ede8 80%, #ffffff 100%);
  }
  .cover-question {
    position: absolute; right: 13px; top: 184px; text-align: right;
    font-family: "Cinzel", Georgia, serif; font-size: 28px; line-height: 35px; color: var(--slate);
  }
  .cover-accent { position: absolute; left: 0; top: 553px; }
  .cover-tagline {
    position: absolute; left: 14px; top: 690px;
    font-family: "Cinzel", Georgia, serif; font-weight: 700; color: var(--slate-dark); line-height: 1;
  }
  .cover-tagline .small { display: block; font-size: 38px; margin-bottom: 18px; }
  .cover-tagline .large { display: block; font-size: 52px; margin-bottom: 14px; }
</style>
</head>
<body>
<div class="canvas">
  <div class="brochure">

    <section class="panel panel--story">
      <p class="story-text">Lorem Ipsum is simply dummy text of the printing and typesetting industry. Lorem Ipsum has been the industry's standard dummy text ever since the 1500s, when an unknown printer took a galley of type and scrambled it to make a type specimen book. It has survived not only five centuries, but also the leap into electronic typesetting, remaining essentially unchanged. It was popularised in the 1960s with the release of Letraset sheets containing Lorem Ipsum</p>
      <div class="story-photo" role="img" aria-label="Photo of a caregiver in blue scrubs smiling with a senior woman seated by a bed"></div>
    </section>

    <section class="panel panel--services">
      <h2 class="services-head">Our company that offers</h2>
      <h3 class="services-title">'ONE STOP SHOP'</h3>
      <p class="services-intro">resources for seniors who<br>need assistance with</p>
      <ul class="services-list">
        <li>selling their home,</li>
        <li>need home care support</li>
        <li>need to find suitable<span class="cont">senior housing living choices</span></li>
        <li>much more</li>
      </ul>
      <div class="brand">
        <span class="brand-mark"></span>
        <span class="brand-name">Maplecrest</span>
        <span class="brand-sub">Senior Resource Group</span>
      </div>
      <p class="address">4820 Cedar Hollow Road, Suite 210<br>Brookfield, WA. 98000</p>
      <div class="contact-band">Call us : (800) 555-0142<br>Email us : info@maplecrestrg.com</div>
    </section>

    <section class="panel panel--cover">
      <div class="brand">
        <span class="brand-mark"></span>
        <span class="brand-name">Maplecrest</span>
        <span class="brand-sub">Senior Resource Group</span>
      </div>
      <div class="cover-photo" role="img" aria-label="Portrait of a senior woman with blonde hair in a white shirt"></div>
      <p class="cover-question">'What's<br>Next?</p>
      <svg class="cover-accent" width="376" height="318" viewBox="0 0 376 318" aria-hidden="true">
        <polygon points="0,52 281,52 281,125 376,0 376,318 0,318" fill="var(--gold)"/>
      </svg>
      <p class="cover-tagline">
        <span class="small">WE WILL</span>
        <span class="large">TAKE CARE</span>
        <span class="small">OF YOU</span>
      </p>
    </section>

  </div>
</div>
</body>
</html>
```